Rally 84 Training is our company name. and instruction

We provide emergency medical training for CPR (Cardiopulmonary Resuscitation) /AED (Automated External Defibrillation) , BLS (Basic Life Support, First Aid, Bloodborne Pathogens
We travel to the client, give certified (CVL) Continental Vitality League (CVL) instruction for job/industry certification in the areas listed.
CVL Kin and Neighbors noncertified instruction

Target Market(s)

Medical professionals, job required certification

Industry/Entity Type

Medical And Science

Contact Information for Business Card

Logo
Phone, email, address, website address, FB, Instagram

Font styles to use
Serif
Sans Serif

Colors
fff2fe
ff1b2f

Requirements
Must have
• Logo
Course taught: CPR (Cardiopulmonary Resuscitation)
AED (Automated External Defibrillation)
First Aid
BLS (Basic Life Support)
Bloodborne Pathogens
Offsite instruction - we come to you
Nice to have
• Red/Black scheme
Possible ecg/heart rhythm design
Should not have
• Cartoon images

```html
<!DOCTYPE html>
<html lang="en">
<head>
<meta charset="utf-8">
<title>Rally 84 Training – Business Card</title>
<link rel="stylesheet" href="https://fonts.googleapis.com/css2?family=Didact+Gothic&family=Mulish:wght@600&display=swap">
<style>
  :root {
    --page: #efefef;
    --card-light: #3f3b3c;
    --card-dark: #1e1b1c;
    --ink: #e9e6e7;
    --ink-soft: #cfcbcc;
    --accent: #d8232c;
    --rule: #8d898a;
  }
  * { box-sizing: border-box; margin: 0; padding: 0; }
  html, body { width: 1200px; height: 800px; overflow: hidden; }
  body {
    background: var(--page);
    font-family: "Didact Gothic", sans-serif;
    color: var(--ink);
    position: relative;
  }
  .card {
    position: absolute;
    top: 250px;
    width: 520px;
    height: 297px;
    background: linear-gradient(135deg, var(--card-light) 0%, #2c2829 55%, var(--card-dark) 100%);
    box-shadow: 0 14px 28px rgba(0,0,0,0.22);
    overflow: hidden;
  }
  .card--front { left: 50px; }
  .card--back { left: 630px; }

  .accent-tab {
    position: absolute;
    right: 0;
    top: 118px;
    width: 40px;
    height: 98px;
    background: var(--accent);
  }

  /* front */
  .brand {
    position: absolute;
    left: 300px;
    top: 150px;
    display: flex;
    align-items: center;
    gap: 8px;
  }
  .brand__dot {
    width: 14px;
    height: 14px;
    border-radius: 50%;
    background: var(--accent);
    flex: none;
  }
  .brand__name {
    font-size: 17px;
    color: var(--ink);
    letter-spacing: 0.3px;
  }
  .courses {
    position: absolute;
    left: 118px;
    top: 178px;
    list-style: none;
    font-size: 11.5px;
    line-height: 18px;
    color: var(--ink-soft);
  }
  .courses li { position: relative; padding-left: 14px; }
  .courses li::before {
    content: "";
    position: absolute;
    left: 0;
    top: 7px;
    width: 4px;
    height: 4px;
    background: var(--accent);
  }
  .courses .gap { display: inline-block; width: 14px; }

  /* back */
  .identity {
    position: absolute;
    left: 0;
    top: 0;
    width: 84px;
    height: 297px;
    display: flex;
    align-items: center;
    justify-content: center;
    gap: 4px;
    writing-mode: vertical-rl;
    transform: rotate(180deg);
  }
  .identity__name {
    font-family: "Mulish", sans-serif;
    font-weight: 600;
    font-size: 19px;
    letter-spacing: 0.8px;
    color: #ffffff;
    white-space: nowrap;
  }
  .identity__role {
    font-size: 11px;
    color: var(--ink-soft);
    align-self: flex-start;
    margin-top: 34px;
  }
  .divider {
    position: absolute;
    left: 84px;
    top: 0;
    width: 1px;
    height: 258px;
    background: var(--rule);
  }
  .contact {
    position: absolute;
    left: 124px;
    top: 190px;
    list-style: none;
    font-size: 11.5px;
    line-height: 17px;
    color: var(--ink-soft);
  }
  .contact__label {
    display: inline-block;
    width: 16px;
    color: var(--ink);
  }
</style>
</head>
<body>
  <section class="card card--front" aria-label="Card front">
    <div class="accent-tab"></div>
    <div class="brand">
      <span class="brand__dot"></span>
      <span class="brand__name">Rally 84 Training</span>
    </div>
    <ul class="courses">
      <li>AED (Automated External Defibrillation)</li>
      <li>First Aid<span class="gap"></span>BLS (Basic Life Support)</li>
      <li>Bloodborne Pathogens</li>
      <li>Offsite instruction - we come to you</li>
    </ul>
  </section>

  <section class="card card--back" aria-label="Card back">
    <div class="accent-tab"></div>
    <div class="identity">
      <span class="identity__name">Marios Kelaidis</span>
      <span class="identity__role">Doctor</span>
    </div>
    <div class="divider"></div>
    <ul class="contact">
      <li><span class="contact__label">A</span>27 Orfeos Str, 14561 Kifisia</li>
      <li><span class="contact__label">D</span>2104417258</li>
      <li><span class="contact__label">M</span>6945203916</li>
      <li><span class="contact__label">E</span>84@rallytraining.com</li>
    </ul>
  </section>
</body>
</html>
```